Oil and Gas Company: Letterhead Design

In short we need a professional company letterhead designed for our Oil and Gas company.

We would like to keep the design simple and professional. Letterhead to include the company logo and color scheme, front page and continuation pages.

For reference, see attached logo below with our company logo and color scheme.

Target Market(s)

Oil & Gas Market

Industry/Entity Type

Oil And Gas

Font styles to use
Sans Serif

Requirements
Must have
• Letterhead must contain a front page & continuation page.
• Must be simple and professional in design.
• Follow our logo and color scheme.
Nice to have
• I would like to have the logo embedded in the bottom right hand portion of the page to provide some depth into the letterhead.

```html
<!DOCTYPE html>
<html lang="en">
<head>
<meta charset="utf-8">
<title>Meridian Field Services — Letterhead</title>
<link href="https://fonts.googleapis.com/css2?family=Poppins:wght@400;500;600&display=swap" rel="stylesheet">
<style>
  :root {
    --backdrop: #d3e5e3;
    --paper: #eeeeee;
    --ink: #2b2b2b;
    --ink-soft: #6a6a6a;
    --body-text: #7a7a7a;
    --brand-blue: #123d8c;
    --brand-red: #cc1420;
    --divider: #b5b5b5;
  }
  * { margin: 0; padding: 0; box-sizing: border-box; }
  html, body { width: 1200px; height: 956px; overflow: hidden; }
  body {
    background: var(--backdrop);
    font-family: "Poppins", sans-serif;
    position: relative;
  }
  .sheet {
    position: absolute;
    top: 124px;
    width: 505px;
    height: 714px;
    background: linear-gradient(180deg, #e9e9e9 0%, var(--paper) 45%, #ebebeb 100%);
  }
  .sheet--front { left: 56px; }
  .sheet--continuation { left: 649px; }

  .company-name {
    position: absolute;
    top: 100px;
    left: 0;
    width: 100%;
    text-align: center;
    font-size: 11px;
    font-weight: 400;
    letter-spacing: 0.6px;
    line-height: 12px;
    color: var(--ink);
  }

  .recipient {
    position: absolute;
    top: 204px;
    left: 46px;
    font-size: 9.2px;
    line-height: 11.6px;
    color: var(--ink-soft);
    letter-spacing: 0.3px;
  }
  .recipient .name, .recipient .role { font-weight: 600; color: #444; }

  .letter-date {
    position: absolute;
    top: 235px;
    right: 44px;
    font-size: 9px;
    color: var(--ink-soft);
    letter-spacing: 0.3px;
  }

  .letter-body {
    position: absolute;
    top: 312px;
    left: 46px;
    width: 415px;
    font-size: 7.3px;
    line-height: 15.2px;
    color: var(--body-text);
    text-align: justify;
    letter-spacing: 0.15px;
  }
  .letter-body p { text-indent: 12px; margin-bottom: 15px; }

  .footer-address {
    position: absolute;
    top: 663px;
    left: 0;
    width: 100%;
    text-align: center;
    font-size: 7px;
    color: #333;
  }
  .footer-address strong { font-weight: 600; }

  .footer-contacts {
    position: absolute;
    top: 677px;
    left: 0;
    width: 100%;
    display: flex;
    justify-content: center;
    align-items: center;
    font-size: 7px;
    color: #333;
  }
  .contact-item { display: flex; align-items: center; gap: 4px; padding: 0 7px; }
  .contact-item + .contact-item { border-left: 1px solid var(--divider); }
  .contact-item svg { width: 9px; height: 9px; }

  .depth-mark {
    position: absolute;
    right: 18px;
    bottom: 26px;
    width: 44px;
    height: 44px;
    border-radius: 50%;
    background: rgba(0, 0, 0, 0.035);
  }

  .brand-band {
    position: absolute;
    left: 0;
    bottom: 0;
    width: 505px;
    height: 10px;
  }
</style>
</head>
<body>

<section class="sheet sheet--front" aria-label="Letterhead front page">
  <div class="company-name">MERIDIAN<br>FIELD SERVICES</div>

  <div class="recipient">
    <div class="name">MR. Daniel HARPER</div>
    <div class="role">Managing Director</div>
    <div>12/08 Cedar Court</div>
    <div>Nevada - 987654321</div>
  </div>

  <div class="letter-date">Date : 01 July 2018</div>

  <div class="letter-body">
    <p>Lorem ipsum dolor sit amet, justo platonem in per, dicant constituto ne eam. Aeque persecuti sit ea, at vis commodo tractatos vituperata, sea an albucius forensibus. Wisi quodsi id qui, duo tempor aliquam assentior eu, no diceret tibique definiebas mei. Id nec noster facilisi mandamus.</p>
    <p>Nullam definiebas signiferumque pro te, vel mutat lobortis conceptam in. Usu justo minimum an, ne regione sanctus praesent usu, eam ut adipisci volutpat. Vel odio tibique consequat ne, in dicit gubergren appellantur vis, quo ei omnis elitr. Qui ne enim dictas dissentiet, pro nulla quodsi deseruisse te. Vide prima eloquentiam pro ei, agam dicta in pro, eu persius propriae constituam sea. Ius ut iriure oblique laboramus, cu sed fugit commune invenire, viris repudiandae ex vis. Nullam definiebas signiferumque pro te, vel mutat lobortis conceptam in. Usu justo minimum an, ne regione sanctus praesent usu, eam ut adipisci volutpat. Vel odio tibique consequat ne, in dicit gubergren appellantur vis, quo ei omnis elitr. Qui ne enim dictas dissentiet, pro nulla quodsi deseruisse te. Vide prima eloquentiam pro ei, agam dicta in pro, eu persius propriae constituam sea. Ius ut iriure oblique laboramus, cu sed fugit commun.</p>
  </div>

  <div class="footer-address"><strong>Meridian Field Services</strong>- 114 N Ridge Avenue, Carter, TX 75001</div>
  <div class="footer-contacts">
    <span class="contact-item">
      <svg viewBox="0 0 10 10"><path d="M2 1 L3.6 1 L4.3 3 L3.2 3.8 Q4 5.8 6.2 6.8 L7 5.7 L9 6.4 L9 8 Q8.6 9 7.6 9 Q2.6 8.4 1 2.4 Q1 1.4 2 1Z" fill="var(--brand-red)"/></svg>
      000 000 0000
    </span>
    <span class="contact-item">
      <svg viewBox="0 0 10 10"><rect x="0.8" y="2" width="8.4" height="6" fill="none" stroke="var(--brand-red)" stroke-width="0.9"/><path d="M0.8 2 L5 5.4 L9.2 2" fill="none" stroke="var(--brand-red)" stroke-width="0.9"/></svg>
      info@yourwebsite.com
    </span>
    <span class="contact-item">
      <svg viewBox="0 0 10 10" fill="none" stroke="var(--brand-red)" stroke-width="0.8"><circle cx="5" cy="5" r="4"/><ellipse cx="5" cy="5" rx="1.8" ry="4"/><path d="M1 5 H9 M1.6 3 H8.4 M1.6 7 H8.4"/></svg>
      www.yourwebsite.com
    </span>
  </div>

  <div class="depth-mark"></div>
  <svg class="brand-band" viewBox="0 0 505 10" preserveAspectRatio="none">
    <polygon points="0,2 432,2 427,10 0,10" fill="var(--brand-blue)"/>
    <polygon points="438,0 505,0 505,10 430,10" fill="var(--brand-red)"/>
  </svg>
</section>

<section class="sheet sheet--continuation" aria-label="Letterhead continuation page">
  <div class="depth-mark"></div>
  <svg class="brand-band" viewBox="0 0 505 10" preserveAspectRatio="none">
    <polygon points="0,2 423,2 418,10 0,10" fill="var(--brand-blue)"/>
    <polygon points="429,0 505,0 505,10 421,10" fill="var(--brand-red)"/>
  </svg>
</section>

</body>
</html>
```